Business Card Stationary and shirt design for Electrical Company
Corbishaw Electric LLC
Business Card Stationary and shirt design for Electrical Company - Construction
Creative Brief
Bright & Fun-filled
Owner
48 Quillmere Lane, Tarnbrook Heights
555-0148
corbishawelectricllc@brivanmail.com
www.corbishawelectric-example.com
Highly rated : TradeRankr, Zorvik, NestGauge residential, commercial, industrial
Name of Business Logo web adress simple yet eye catching back (ill leave it up to the designer)

```html
<!DOCTYPE html>
<html lang="en">
<head>
<meta charset="utf-8">
<title>Corbishaw Electric LLC – Stationery and Shirt Set</title>
<link rel="stylesheet" href="https://fonts.googleapis.com/css2?family=Montserrat:wght@400;600;700&display=swap">
<style>
  :root{
    --bg:#3b3c3e;
    --paper:#ffffff;
    --navy:#1f2a44;
    --flap:#26335a;
    --green:#8cc63f;
    --grey:#9a9ca0;
    --ink:#444;
  }
  *{box-sizing:border-box;margin:0;padding:0}
  html,body{width:1200px;height:245px;overflow:hidden;background:var(--bg);font-family:"Montserrat",sans-serif}
  .canvas{position:relative;width:1200px;height:245px}
  .piece{position:absolute;background:var(--paper);box-shadow:0 2px 6px rgba(0,0,0,.35);overflow:hidden}
  .brand{display:flex;align-items:center;gap:4px;color:var(--navy);font-weight:700;white-space:nowrap;line-height:1}
  .brand .mark{background:var(--green);flex:none}
  .brand.light{color:#fff}

  .hero-brand{position:absolute;left:24px;top:86px;font-size:14px}
  .hero-brand .mark{width:14px;height:14px}

  .card{width:92px;height:52px}
  .card-front{display:flex;align-items:center;justify-content:center;font-size:6px}
  .card-front .mark{width:7px;height:7px}
  .card-back{background:var(--navy);padding:6px;color:#fff;font-size:3.4px;line-height:1.5}
  .card-back .title{font-weight:700;font-size:4.4px;margin-bottom:3px}
  .card-back .bar{position:absolute;left:0;bottom:0;width:100%;height:6px;background:var(--green)}
  .badges{display:flex;gap:4px;margin-bottom:3px}
  .badge{width:10px;height:10px;background:var(--green)}

  .letter{top:16px;width:128px;height:204px;padding:10px;font-size:3.4px;color:var(--ink);line-height:1.6}
  .letter .brand{font-size:6px;margin-bottom:14px}
  .letter .brand .mark{width:7px;height:7px}
  .letter p{margin-bottom:6px}
  .letter .sign{margin-top:14px;color:var(--navy);font-weight:600}
  .letter .contact{position:absolute;left:0;bottom:0;width:100%;padding:4px 10px;border-top:3px solid var(--green);font-size:3px;color:var(--navy)}
  .watermark{position:absolute;right:10px;top:80px;width:50px;height:50px;background:var(--green);opacity:.08}

  .small-card{width:64px;height:36px;padding:5px;font-size:3.6px}
  .small-card .mark{width:5px;height:5px}
  .small-card.dark{background:var(--navy)}
  .small-card .bar{position:absolute;left:0;bottom:0;width:100%;height:4px;background:var(--green)}

  .envelope{left:700px;width:180px;height:78px;padding:7px;font-size:5px}
  .envelope .mark{width:6px;height:6px}
  .envelope .addr{font-size:3px;color:var(--grey);margin-top:3px;line-height:1.5}
  .envelope.back{background:var(--navy)}
  .envelope .flap{position:absolute;left:0;top:0}
  .envelope .stripe{position:absolute;left:0;bottom:0;width:100%;height:5px;background:var(--green)}

  .shirt-print{width:62px;height:100px;padding:4px;display:flex;flex-direction:column;align-items:center;justify-content:center;gap:4px;font-size:4.4px;text-align:center}
  .shirt-print .mark{width:6px;height:6px}
  .shirt-print .tag{font-size:3px;color:var(--green);font-weight:600;overflow-wrap:anywhere}
</style>
</head>
<body>
<main class="canvas">

  <div class="brand hero-brand light"><span class="mark"></span>Corbishaw Electric LLC</div>

  <!-- Business cards -->
  <section class="piece card card-front" style="left:24px;top:110px"><div class="brand"><span class="mark"></span>Corbishaw Electric LLC</div></section>
  <section class="piece card card-back" style="left:24px;top:170px">
    <div class="title">Owner</div>
    <div>48 Quillmere Lane, Tarnbrook Heights</div>
    <div>555-0148</div>
    <div>corbishawelectricllc@brivanmail.com</div>
    <div>www.corbishawelectric-example.com</div>
    <span class="bar"></span>
  </section>
  <section class="piece card card-front" style="left:122px;top:110px"><div class="brand"><span class="mark"></span>Corbishaw Electric LLC</div></section>
  <section class="piece card card-back" style="left:122px;top:170px">
    <div class="title">Highly rated</div>
    <div class="badges"><span class="badge"></span><span class="badge"></span><span class="badge"></span></div>
    <div>TradeRankr · Zorvik · NestGauge</div>
    <div>Residential · Commercial · Industrial</div>
    <span class="bar"></span>
  </section>

  <!-- Letterheads -->
  <article class="piece letter" style="left:250px">
    <div class="brand"><span class="mark"></span>Corbishaw Electric LLC</div>
    <span class="watermark"></span>
    <p>Thank you for choosing us for safe, reliable residential, commercial and industrial electrical work.</p>
    <div class="sign">Sincerely,<br>Owner</div>
    <div class="contact">48 Quillmere Lane, Tarnbrook Heights · 555-0148<br>www.corbishawelectric-example.com</div>
  </article>
  <article class="piece letter" style="left:392px">
    <div class="brand"><span class="mark"></span>Corbishaw Electric LLC</div>
    <span class="watermark"></span>
    <p>Thank you for choosing us for safe, reliable residential, commercial and industrial electrical work.</p>
    <div class="sign">Sincerely,<br>Owner</div>
    <div class="contact">48 Quillmere Lane, Tarnbrook Heights · 555-0148<br>www.corbishawelectric-example.com</div>
  </article>

  <!-- Compliment cards -->
  <section class="piece small-card" style="left:540px;top:82px"><div class="brand"><span class="mark"></span>Corbishaw Electric LLC</div><span class="bar"></span></section>
  <section class="piece small-card dark" style="left:610px;top:82px"><div class="brand light"><span class="mark"></span>Corbishaw Electric LLC</div><span class="bar"></span></section>
  <section class="piece small-card" style="left:540px;top:124px"><div class="brand"><span class="mark"></span>Corbishaw Electric LLC</div><span class="bar"></span></section>
  <section class="piece small-card dark" style="left:610px;top:124px"><div class="brand light"><span class="mark"></span>Corbishaw Electric LLC</div><span class="bar"></span></section>

  <!-- Envelopes -->
  <section class="piece envelope back" style="top:74px">
    <svg class="flap" width="180" height="44" viewBox="0 0 180 44"><path d="M0 0 L90 40 L180 0 Z" fill="var(--flap)"/></svg>
    <span class="stripe"></span>
  </section>
  <section class="piece envelope" style="top:158px;height:62px">
    <div class="brand"><span class="mark"></span>Corbishaw Electric LLC</div>
    <div class="addr">48 Quillmere Lane<br>Tarnbrook Heights</div>
    <span class="stripe"></span>
  </section>

  <!-- Shirt prints -->
  <section class="piece shirt-print" style="left:920px;top:14px"><div class="brand"><span class="mark"></span>Corbishaw</div><span class="tag">Electric LLC</span></section>
  <section class="piece shirt-print" style="left:988px;top:14px"><span class="tag">555-0148</span></section>
  <section class="piece shirt-print" style="left:1056px;top:14px"><div class="brand"><span class="mark"></span>Corbishaw</div><span class="tag">Electric LLC</span></section>
  <section class="piece shirt-print" style="left:1124px;top:14px"><span class="tag">www.corbishawelectric-example.com</span></section>
  <section class="piece shirt-print" style="left:920px;top:124px"><div class="brand"><span class="mark"></span>Corbishaw</div><span class="tag">Electric LLC</span></section>
  <section class="piece shirt-print" style="left:988px;top:124px"><span class="tag">555-0148</span></section>
  <section class="piece shirt-print" style="left:1056px;top:124px"><div class="brand"><span class="mark"></span>Corbishaw</div><span class="tag">Electric LLC</span></section>
  <section class="piece shirt-print" style="left:1124px;top:124px"><span class="tag">Residential · Commercial</span></section>

</main>
</body>
</html>
```